Tallow Ridge Advisory WordPress Site.

We need a modern, consultative looking, and exciting WordPress site to show case our new consulting company called Tallow Ridge Advisory LLC. Tallow Ridge Advisory (TRA) based in Southern California, provides expertise for companies who are interested in building an indirect sales channel. Some may think of this as building a Partner Program. Our offerings include, Discovery, Strategic Planning, Goals and Objective Setting, Partner Recruitment & Enablement, Team Building, and Outcome Definition. We purchased our logo from Fernquill which is attached. The colors are Blue and Grey. The final design should convey a fresh, modern, and exciting look. Don't forget this is a consulting company, so we can't get too "wild". Hopefully we can come up with a nice balance. We attached our logo (two versions) and our Founder's photo. Please let us know what else you need to get started. I suspect you'll outline the design and we can iterate on the copy. Lastly, we'll be using Brookvane as our hosting provider.

Target Market(s)

Small to mid-size SaaS Companies.

Industry/Entity Type

Consulting for Indirect Sales Channels

Coding

Coded - Design and coding required

Font styles to use
Other font styles liked:
• Please select a font that compliments the logo. Modern and easy to read.

Colors
0054AA
0677BA
7BADD7
CADEEF
E8F1F8
00AB8E
00BBA5
67D7C9
C6EFE9
E9F9F6
FFF300
FFF600
FEFA6F
FFFEC7
FFFEE8

Requirements
Must have
• My project must include the following pages. Homepage, About Us, Offerings & Services, and Contact Us
Nice to have
• Clean, bright and modern look. Area(s) and ability to insert video or blog posts.
Should not have
• Should not contain clutter. Black background.

```html
<!DOCTYPE html>
<html lang="en">
<head>
<meta charset="utf-8">
<title>Tallow Ridge Advisory</title>
<link href="https://fonts.googleapis.com/css2?family=Poppins:wght@300;400;500;600;700;800&display=swap" rel="stylesheet">
<style>
:root{
  --blue:#0054AA;
  --blue-mid:#0677BA;
  --blue-deep:#0a3680;
  --navy:#0b2452;
  --sky:#7BADD7;
  --ice:#E8F1F8;
  --teal:#00BBA5;
  --ink:#1d2330;
  --grey:#6d7380;
  --paper:#f3f4f6;
  --white:#ffffff;
}
*{margin:0;padding:0;box-sizing:border-box}
html,body{width:1200px;height:3960px;overflow:hidden}
body{font-family:"Poppins",sans-serif;color:var(--ink);background:var(--white);position:relative}
section,header,footer{position:absolute;left:0;width:1200px}
.abs{position:absolute}

/* header */
.site-header{top:0;height:88px;background:var(--white);box-shadow:0 2px 8px rgba(0,0,0,.08);z-index:5}
.brand{left:208px;top:24px;display:flex;align-items:center;gap:10px;font-weight:700;font-size:13px;line-height:1.15;color:var(--blue);letter-spacing:.8px;white-space:nowrap}
.brand-dot{width:36px;height:36px;border-radius:50%;background:var(--blue);flex:none}
.nav{left:464px;top:35px;display:flex;gap:22px;font-size:13px;font-weight:500;color:var(--ink);white-space:nowrap}
.nav .active{color:var(--blue);border-bottom:2px solid var(--blue);padding-bottom:4px}
.call{left:828px;top:22px;width:164px;height:46px;background:var(--blue);color:#fff;border-radius:4px;padding:6px 10px 0 42px;font-size:9px;letter-spacing:.5px;white-space:nowrap}
.call strong{display:block;font-size:15px;letter-spacing:.3px}
.call svg{position:absolute;left:13px;top:13px}

/* hero */
.hero{top:88px;height:672px;background:linear-gradient(120deg,#0a2a6e 0%,#0b4aa0 55%,#0a3b8c 100%);overflow:hidden}
.hero-photo{right:0;top:0;width:520px;height:672px;background:linear-gradient(180deg,#2a5fb0 0%,#1e3c70 60%,#161d2c 100%)}
.hero-rail{left:78px;top:230px;width:2px;height:220px;background:rgba(255,255,255,.4)}
.hero-rail::after{content:"";position:absolute;left:-9px;top:96px;width:20px;height:20px;border-radius:50%;background:#fff}
.hero-copy{left:208px;top:258px;color:#fff}
.hero-copy .kicker{font-size:40px;font-weight:400;letter-spacing:3px}
.hero-copy h1{font-size:66px;font-weight:800;line-height:1;letter-spacing:1px;margin-top:2px}
.hero-copy p{font-size:15px;margin-top:16px;font-weight:500}
.btn-light{display:inline-block;margin-top:26px;background:#fff;color:var(--ink);font-size:14px;font-weight:600;padding:10px 26px;border-radius:3px}

/* section 01 */
.worry{top:760px;height:440px;background:var(--white)}
.laptop{left:180px;top:82px;width:380px;height:246px}
.laptop .screen{position:absolute;left:20px;top:0;width:340px;height:220px;background:#111;border-radius:8px;padding:10px}
.laptop .screen div{width:100%;height:100%;background:linear-gradient(135deg,#d9d3cc,#8b7f78 60%,#4a4a52)}
.laptop .base{position:absolute;left:0;top:220px;width:380px;height:14px;background:#c9ccd2;border-radius:0 0 10px 10px}
.num{font-size:120px;font-weight:800;color:#eceef1;line-height:1}
.worry .num{left:610px;top:40px}
.block-text{font-size:12.5px;color:var(--grey);line-height:1.45}
.block-title{font-size:25px;font-weight:700;line-height:1.25;color:var(--ink)}
.worry .copy{left:620px;top:132px;width:380px}

/* section 02 */
.options{top:1200px;height:560px;background:linear-gradient(180deg,#2e2f33,#1c1d21);overflow:hidden}
.options .num{left:540px;top:20px;color:rgba(255,255,255,.08)}
.options h2{left:0;width:1200px;top:104px;text-align:center;color:#fff;font-size:26px;font-weight:700}
.options p{left:220px;width:760px;top:150px;text-align:center;color:#e3e4e8;font-size:13px;line-height:1.55}
.card{top:280px;width:184px;height:160px;border:1px solid rgba(255,255,255,.6);border-radius:6px;display:flex;flex-direction:column;align-items:center;justify-content:center;gap:14px;color:#fff;font-size:14px;font-weight:500;text-align:center;line-height:1.2}
.card.on{background:#fff;color:var(--ink)}
.dots{display:flex;gap:10px}
.dots i{width:10px;height:10px;border-radius:50%;background:#fff;opacity:.5}
.dots i.on{opacity:1}

/* section 03 */
.scale{top:1760px;height:560px;background:var(--white)}
.scale .num{left:200px;top:70px}
.scale .copy{left:208px;top:160px;width:340px}
.scale .block-title{font-size:24px}
.tile{background:linear-gradient(135deg,#c4bcb4,#7b706a);border:4px solid #fff}

/* section 04 */
.benefits{top:2320px;height:400px;background:linear-gradient(180deg,#0a3f95,#0b4aa8);overflow:hidden}
.benefits .num{left:540px;top:10px;color:rgba(255,255,255,.08)}
.benefits h2{left:0;width:1200px;top:104px;text-align:center;color:#fff;font-size:27px;font-weight:700}
.benefit{top:198px;width:120px;text-align:center;color:#fff;font-size:13px;font-weight:600;line-height:1.2}
.benefit .ic{width:68px;height:68px;border-radius:50%;background:#fff;margin:0 auto 10px;display:flex;align-items:center;justify-content:center}

/* testimonials */
.testimonials{top:2720px;height:520px;background:var(--paper)}
.testimonials h2{left:0;width:1200px;top:56px;text-align:center;font-size:26px;font-weight:700}
.quote{top:122px;width:384px;height:278px;padding:26px 26px;font-size:11.5px;line-height:1.55;border-radius:2px}
.quote.featured{left:208px;background:var(--blue);color:#fff}
.quote.plain{left:608px;background:#fff;color:var(--grey);box-shadow:0 4px 14px rgba(0,0,0,.06)}
.author{position:absolute;left:26px;bottom:40px;display:flex;gap:10px;align-items:center}
.avatar{width:34px;height:34px;border-radius:50%;background:var(--sky)}
.author b{display:block;font-size:12px}
.author small{font-size:9px;opacity:.8}
.stars{position:absolute;left:26px;bottom:20px;color:var(--teal);font-size:14px;letter-spacing:2px}
.qmark{position:absolute;right:22px;bottom:6px;font-size:120px;font-weight:800;line-height:.8;font-family:Georgia,serif}
.featured .qmark{color:rgba(255,255,255,.3)}
.plain .qmark{color:#eceef1}
.arrow{top:250px}

/* contact */
.contact{top:3240px;height:656px;background:linear-gradient(180deg,#2a2b30 0%,#202126 60%,#1b2a4a 100%);overflow:hidden}
.contact h2{left:0;width:1200px;top:64px;text-align:center;color:#fff;font-size:27px;font-weight:700}
.field{left:380px;width:440px;height:40px;background:#fff;border-radius:2px;font-size:12px;color:#9aa0aa;padding:11px 12px}
.field.msg{height:140px}
.send{left:380px;width:440px;height:40px;top:448px;background:var(--blue);color:#fff;font-size:13px;font-weight:600;text-align:center;line-height:40px;letter-spacing:1px}
.contact-row{top:592px;color:#fff;font-size:14px;display:flex;align-items:center;gap:10px;white-space:nowrap}
.ic-ring{width:32px;height:32px;border-radius:50%;border:1.5px solid #fff;display:flex;align-items:center;justify-content:center}

/* footer */
.site-footer{top:3896px;height:64px;background:var(--blue-deep);color:#fff}
.site-footer p{position:absolute;left:208px;top:24px;font-size:10.5px;letter-spacing:.5px}
.social{position:absolute;right:208px;top:18px;display:flex;gap:10px}
.social i{width:26px;height:26px;border-radius:50%;background:#fff;opacity:.9}
</style>
</head>
<body>

<header class="site-header">
  <div class="abs brand"><span class="brand-dot"></span><span>TALLOW RIDGE<br>ADVISORY</span></div>
  <nav class="abs nav"><span class="active">Home</span><span>Our Services</span><span>Testimonials</span><span>Contact Us</span></nav>
  <div class="abs call">
    <svg width="20" height="20" viewBox="0 0 24 24" fill="#fff"><path d="M6.6 10.8a15 15 0 0 0 6.6 6.6l2.2-2.2a1 1 0 0 1 1-.25 11.4 11.4 0 0 0 3.6.6 1 1 0 0 1 1 1V20a1 1 0 0 1-1 1A17 17 0 0 1 3 4a1 1 0 0 1 1-1h3.5a1 1 0 0 1 1 1c0 1.25.2 2.45.6 3.6a1 1 0 0 1-.25 1z"/></svg>
    CALL US NOW<strong>555-010-4821</strong>
  </div>
</header>

<section class="hero">
  <div class="abs hero-photo" role="img" aria-label="Founder portrait in a dark suit against a blue city skyline"></div>
  <div class="abs hero-rail"></div>
  <div class="abs hero-copy">
    <div class="kicker">CONTROL</div>
    <h1>YOUR FUTURE</h1>
    <p>Create • Optimize • Unleash the Power of Partnerships &amp; Alliances</p>
    <span class="btn-light">Get Started</span>
  </div>
</section>

<section class="worry">
  <div class="abs laptop">
    <div class="screen"><div role="img" aria-label="Business team meeting around a table"></div></div>
    <div class="base"></div>
  </div>
  <div class="abs num">01</div>
  <div class="abs copy">
    <h2 class="block-title">Do You Worry About How You're Going To Make Your Revenue Number While Managing Costs?</h2>
    <p class="block-text" style="margin-top:6px">You're not alone. Most business leaders wrestle with the same concern.</p>
  </div>
</section>

<section class="options">
  <div class="abs num">02</div>
  <h2 class="abs">What options do you have?</h2>
  <p class="abs">You can hire more salespeople and business development reps. You can invest in Search Ads, marketing campaigns, purchase lead lists, conduct webinars, increase social marketing, train your sales team, add solution engineers, etc. You get the picture...</p>
  <div class="abs card" style="left:208px"><svg width="44" height="44"><rect x="6" y="6" width="32" height="32" rx="6" fill="#fff" opacity=".9"/></svg>Search Ads</div>
  <div class="abs card on" style="left:408px"><svg width="44" height="44" viewBox="0 0 44 44" fill="none" stroke="#3a4150" stroke-width="2.5"><rect x="6" y="8" width="32" height="22" rx="2"/><path d="M12 24l7-7 6 5 7-8"/><path d="M16 36h12M22 30v6"/></svg>Marketing<br>Campaigns</div>
  <div class="abs card" style="left:608px"><svg width="44" height="44" viewBox="0 0 44 44" fill="#fff"><circle cx="22" cy="14" r="6"/><circle cx="10" cy="18" r="4.5"/><circle cx="34" cy="18" r="4.5"/><path d="M12 36a10 10 0 0 1 20 0z"/><path d="M2 34a8 8 0 0 1 12-6l-2 6zM42 34a8 8 0 0 0-12-6l2 6z"/></svg>Sales Team</div>
  <div class="abs card" style="left:808px"><svg width="44" height="44" viewBox="0 0 44 44" fill="none" stroke="#fff" stroke-width="2.5"><rect x="6" y="6" width="32" height="24" rx="3"/><circle cx="15" cy="18" r="3"/><circle cx="29" cy="18" r="3"/><path d="M18 18h8M22 30v6M14 38h16"/></svg>Social<br>Marketing</div>
  <div class="abs dots" style="left:570px;top:484px"><i class="on"></i><i></i><i></i></div>
</section>

<section class="scale">
  <div class="abs num">03</div>
  <div class="abs copy">
    <h2 class="block-title">Have you considered scaling your business through partnerships and alliances?</h2>
    <p class="block-text" style="margin-top:10px">Do you really know what that means? Does your strategic plan include a robust indirect sales channel? If not, it should.</p>
  </div>
  <div class="abs tile" style="left:600px;top:40px;width:210px;height:250px" role="img" aria-label="Professional woman smiling at work"></div>
  <div class="abs tile" style="left:810px;top:40px;width:190px;height:130px;background:linear-gradient(135deg,#b8a89c,#5c5048)" role="img" aria-label="Businessman portrait"></div>
  <div class="abs tile" style="left:810px;top:170px;width:190px;height:170px;background:linear-gradient(135deg,#cfc6be,#8c8078)" role="img" aria-label="Two colleagues shaking hands"></div>
  <div class="abs tile" style="left:600px;top:290px;width:210px;height:140px;background:linear-gradient(135deg,#d6cfc8,#9c8f86)" role="img" aria-label="Team reviewing documents"></div>
</section>

<section class="benefits">
  <div class="abs num">04</div>
  <h2 class="abs">An indirect sales channel can open the door to...</h2>
  <div class="abs benefit" style="left:188px"><div class="ic"><svg width="30" height="30" viewBox="0 0 30 30" fill="none" stroke="#0054AA" stroke-width="2.5"><path d="M9 4v9a6 6 0 0 0 12 0V4M9 4h4M17 4h4M15 19v7"/></svg></div>Lead<br>Generation</div>
  <div class="abs benefit" style="left:306px"><div class="ic"><svg width="30" height="30" viewBox="0 0 30 30" fill="none" stroke="#0054AA" stroke-width="2.5"><path d="M8 22c-2-6 4-16 16-18-2 12-12 18-18 16zM6 24l5-5M16 10l4 4"/></svg></div>Deal<br>Acceleration</div>
  <div class="abs benefit" style="left:424px"><div class="ic"><svg width="30" height="30" viewBox="0 0 30 30" fill="none" stroke="#0054AA" stroke-width="2.5"><path d="M5 25V15M12 25V10M19 25V13M26 25V5"/></svg></div>Higher<br>Close Ratios</div>
  <div class="abs benefit" style="left:542px"><div class="ic"><svg width="30" height="30" viewBox="0 0 30 30" fill="none" stroke="#0054AA" stroke-width="2.5"><circle cx="15" cy="15" r="10"/><circle cx="15" cy="15" r="4"/><path d="M15 2v4M15 24v4M2 15h4M24 15h4"/></svg></div>Cost<br>Management</div>
  <div class="abs benefit" style="left:660px"><div class="ic"><svg width="30" height="30" viewBox="0 0 30 30" fill="none" stroke="#0054AA" stroke-width="2.5"><circle cx="15" cy="15" r="11"/><path d="M15 8v14M11 11h6a2.5 2.5 0 0 1 0 5h-4a2.5 2.5 0 0 0 0 5h6"/></svg></div>Improved<br>Margin</div>
  <div class="abs benefit" style="left:778px"><div class="ic"><svg width="30" height="30" viewBox="0 0 30 30" fill="none" stroke="#0054AA" stroke-width="2.5"><rect x="4" y="4" width="22" height="22"/><path d="M4 18l7-6 5 4 10-8"/></svg></div>Scalability</div>
  <div class="abs benefit" style="left:896px"><div class="ic"><svg width="30" height="30" viewBox="0 0 30 30" fill="none" stroke="#0054AA" stroke-width="2.5"><path d="M4 26h22M7 26V18M13 26V13M19 26V9M25 26V5"/></svg></div>Growth</div>
</section>

<section class="testimonials">
  <h2 class="abs">Our Testimonials</h2>
  <svg class="abs arrow" style="left:112px" width="24" height="24" viewBox="0 0 24 24" fill="none" stroke="#1d2330" stroke-width="3"><path d="M20 12H5M11 5l-7 7 7 7"/></svg>
  <svg class="abs arrow" style="left:1064px" width="24" height="24" viewBox="0 0 24 24" fill="none" stroke="#1d2330" stroke-width="3"><path d="M4 12h15M13 5l7 7-7 7"/></svg>
  <div class="abs quote featured">
    Lorem Ipsum is simply dummy text of the printing and typesetting industry. Lorem Ipsum has been the industry's standard dummy text ever since the 1500s, when an unknown printer took a galley of type and scrambled it to make a type specimen book. It has survived not only five centuries, but also the leap into electronic typesetting, remaining essentially unchanged.
    <div class="author"><span class="avatar"></span><div><b>Marla Quint</b><small>Partner lead, SaaS firm</small></div></div>
    <div class="stars">★★★★★</div>
    <div class="qmark">”</div>
  </div>
  <div class="abs quote plain">
    Lorem Ipsum is simply dummy text of the printing and typesetting industry. Lorem Ipsum has been the industry's standard dummy text ever since the 1500s, when an unknown printer took a galley of type and scrambled it to make a type specimen book. It has survived not only five centuries, but also the leap into electronic typesetting, remaining essentially unchanged.
    <div class="author"><span class="avatar"></span><div><b style="color:#1d2330">Marla Quint</b><small>Partner lead, SaaS firm</small></div></div>
    <div class="stars">★★★★★</div>
    <div class="qmark">”</div>
  </div>
  <div class="abs dots" style="left:570px;top:438px"><i class="on" style="background:#0054AA"></i><i style="background:#0054AA"></i><i style="background:#0054AA"></i></div>
</section>

<section class="contact">
  <div class="abs" style="left:0;top:0;width:1200px;height:656px;background:linear-gradient(90deg,rgba(60,60,66,.5),rgba(30,30,36,.2) 50%,rgba(40,50,80,.5))" role="img" aria-label="Business people in an office, darkened behind the form"></div>
  <h2 class="abs">Contact Us</h2>
  <div class="abs field" style="top:128px">Name</div>
  <div class="abs field" style="top:188px">Email</div>
  <div class="abs field" style="top:248px">Subject</div>
  <div class="abs field msg" style="top:296px">Message</div>
  <div class="abs send">SEND</div>
  <div class="abs contact-row" style="left:208px"><span class="ic-ring"><svg width="14" height="14" viewBox="0 0 24 24" fill="#fff"><path d="M6.6 10.8a15 15 0 0 0 6.6 6.6l2.2-2.2a1 1 0 0 1 1-.25 11.4 11.4 0 0 0 3.6.6 1 1 0 0 1 1 1V20a1 1 0 0 1-1 1A17 17 0 0 1 3 4a1 1 0 0 1 1-1h3.5a1 1 0 0 1 1 1c0 1.25.2 2.45.6 3.6a1 1 0 0 1-.25 1z"/></svg></span>555-010-4821</div>
  <div class="abs contact-row" style="left:500px;font-weight:700;font-size:13px;line-height:1.15;letter-spacing:.8px"><span class="brand-dot" style="background:#fff;width:30px;height:30px"></span><span>TALLOW RIDGE<br>ADVISORY</span></div>
  <div class="abs contact-row" style="left:808px"><span class="ic-ring"><svg width="14" height="14" viewBox="0 0 24 24" fill="none" stroke="#fff" stroke-width="2.4"><rect x="3" y="5" width="18" height="14" rx="1"/><path d="M3 6l9 7 9-7"/></svg></span>info@tallowridge.co</div>
</section>

<footer class="site-footer">
  <p>COPYRIGHT © 2020 RIGHTS RESERVED, TALLOW RIDGE ADVISORY</p>
  <div class="social"><i></i><i></i><i></i><i></i></div>
</footer>

</body>
</html>
```